KTR Football Academy Term 1 Certificate

Hello,
I require a certificate design which will be an improvement on previous designs attached.
The certificate must incorporate both logos and have the wording below.

Kestrel Track Rovers Football Academy
Certificate Of Participation
Presented to
______________________________________________________

For completing KTR Football Academy Term 1, 2024

```html
<!DOCTYPE html>
<html lang="en">
<head>
<meta charset="utf-8">
<title>KTR Football Academy – Certificate of Participation</title>
<link rel="stylesheet" href="https://fonts.googleapis.com/css2?family=Open+Sans:wght@400;700&display=swap">
<style>
  :root {
    --green: #84f51f;
    --green-text: #7fe520;
    --grey: #5d6a70;
    --white: #ffffff;
    --band-green: #e6f9dc;
    --band-pink: #fde6ec;
    --band-green-soft: #effbe6;
  }
  * { margin: 0; padding: 0; box-sizing: border-box; }
  html, body { width: 1200px; height: 849px; overflow: hidden; background: var(--white); }
  body { font-family: "Open Sans", sans-serif; }
  .certificate { position: relative; width: 1200px; height: 849px; overflow: hidden; background: var(--white); }
  .background-bands { position: absolute; inset: 0; }
  .academy-mark {
    position: absolute; left: 47px; top: 44px; width: 161px; height: 214px;
    display: flex; flex-direction: column; align-items: center; justify-content: center; gap: 12px;
    text-align: center;
  }
  .academy-mark .dot { width: 34px; height: 34px; border-radius: 50%; background: var(--green); }
  .academy-mark .name { color: var(--grey); font-weight: 700; font-size: 20px; line-height: 1.15; text-transform: uppercase; }
  .partner-mark {
    position: absolute; left: 935px; top: 60px; width: 220px; height: 130px;
    display: flex; align-items: center; gap: 12px;
  }
  .partner-mark .square { flex: none; width: 30px; height: 30px; background: var(--green); }
  .partner-mark .name { color: var(--green-text); font-weight: 700; font-size: 24px; line-height: 1.05; text-transform: uppercase; }
  .title-block { position: absolute; left: 0; right: 0; top: 186px; text-align: center; }
  .title-primary { color: var(--green-text); font-weight: 700; font-size: 50px; line-height: 52px; letter-spacing: 1px; }
  .title-secondary { color: var(--grey); font-weight: 400; font-size: 43px; line-height: 50px; letter-spacing: 1px; }
  .award-panel {
    position: absolute; left: 325px; top: 311px; width: 549px; height: 220px;
    background: var(--green); border-radius: 22px; color: var(--white); text-align: center;
  }
  .award-heading { margin-top: 20px; font-weight: 700; font-size: 62px; line-height: 72px; }
  .award-sub { font-weight: 400; font-size: 46px; line-height: 54px; }
  .presented { position: absolute; left: 0; right: 0; top: 548px; text-align: center; color: var(--grey); font-size: 39px; line-height: 48px; }
  .name-line { position: absolute; left: 392px; top: 663px; width: 415px; height: 1.5px; background: var(--grey); }
  .completion { position: absolute; left: 0; right: 0; top: 697px; padding-left: 30px; text-align: center; color: var(--grey); font-size: 27px; line-height: 31px; }
  .ball-illustration {
    position: absolute; left: 67px; top: 553px; width: 246px; height: 254px; border-radius: 50%;
    background: radial-gradient(circle at 40% 35%, #f4f6f6 0%, #c8cdcf 60%, #8a9497 100%);
  }
</style>
</head>
<body>
<main class="certificate">
  <svg class="background-bands" width="1200" height="849" viewBox="0 0 1200 849" aria-hidden="true">
    <g transform="rotate(-31 600 425)">
      <rect x="-600" y="-600" width="2400" height="700" fill="var(--band-green-soft)"/>
      <rect x="-600" y="100" width="2400" height="80" fill="var(--white)"/>
      <rect x="-600" y="180" width="2400" height="95" fill="var(--band-pink)"/>
      <rect x="-600" y="275" width="2400" height="55" fill="var(--band-green)"/>
      <rect x="-600" y="330" width="2400" height="40" fill="var(--band-pink)"/>
      <rect x="-600" y="370" width="2400" height="150" fill="var(--white)"/>
      <rect x="-600" y="520" width="2400" height="90" fill="var(--band-green-soft)"/>
      <rect x="-600" y="610" width="2400" height="20" fill="var(--white)"/>
      <rect x="-600" y="630" width="2400" height="70" fill="var(--band-pink)"/>
      <rect x="-600" y="700" width="2400" height="20" fill="var(--white)"/>
      <rect x="-600" y="720" width="2400" height="800" fill="var(--band-green-soft)"/>
    </g>
  </svg>

  <div class="academy-mark">
    <span class="dot"></span>
    <span class="name">KTR Football Academy</span>
  </div>

  <div class="partner-mark">
    <span class="square"></span>
    <span class="name">Kestrel Track Rovers</span>
  </div>

  <header class="title-block">
    <h1 class="title-primary">KESTREL TRACK</h1>
    <p class="title-secondary">ROVERS FOOTBALL ACADEMY</p>
  </header>

  <section class="award-panel">
    <h2 class="award-heading">CERTIFICATE</h2>
    <p class="award-sub">OF</p>
    <p class="award-sub">PARTICIPATION</p>
  </section>

  <p class="presented">PRESENTED TO</p>
  <div class="name-line"></div>

  <p class="completion">FOR COMPLETING<br>KTR FOOTBALL ACADEMY<br>TERM 1,2024</p>

  <div class="ball-illustration" role="img" aria-label="Illustration of a black and white football"></div>
</main>
</body>
</html>
```